Veltora Software Business Card Design

We are a new organization called Veltora. We are a software as a service provider. We deliver a project and program management solution via the internet, so everyone has the ability to work together and collaborate. Its an enterprise platform and we will focus on 50 plus employee company.

We have a website in place
www.veltora-demo.com

Use this as a start of producing the business card. The logo is there as well, but if you have a great and better solution...

Color scheme's could be inline with the website, but don't pin point on it. We can always change the website, logo, color scheme etc.

Target Market(s)

B2B, Projectmembers, projectmanagers, ICT, CTO, Marketing Managers

Industry/Entity Type

Software

Requirements
Must have
• Marten Kuyvelsma

Tel: +31 255 47 09 36
Mob: +31 6 927 15 062
marten@veltora-demo.com
Oostelingpad 84c
2184 KT Duinwijk

Www.veltora-demo.com
social media links

```html
<!DOCTYPE html>
<html lang="en">
<head>
<meta charset="utf-8">
<title>Veltora Business Card</title>
<link rel="stylesheet" href="https://fonts.googleapis.com/css2?family=Exo+2:wght@300;400;700&display=swap">
<style>
  :root {
    --page: #d9d9da;
    --paper: #f4f4f4;
    --lime: #b3bf2b;
    --lime-soft: #a9b833;
    --blue: #1f9cec;
    --orange: #ea7d0b;
    --white: #ffffff;
    --shadow: rgba(0, 0, 0, 0.18);
  }
  * { box-sizing: border-box; margin: 0; padding: 0; }
  html, body {
    width: 1200px;
    height: 861px;
    overflow: hidden;
    background: var(--page);
    font-family: "Exo 2", sans-serif;
  }
  .sheet {
    width: 1200px;
    height: 861px;
    display: flex;
    align-items: center;
    justify-content: center;
    gap: 40px;
  }
  .card {
    position: relative;
    width: 540px;
    height: 309px;
    background: var(--paper);
    box-shadow: 0 10px 28px var(--shadow);
    overflow: hidden;
  }
  .card-shape {
    position: absolute;
    inset: 0;
    width: 100%;
    height: 100%;
  }

  /* contact side */
  .contact .brand {
    position: absolute;
    left: 60px;
    top: 38px;
    font-size: 66px;
    font-weight: 300;
    color: var(--lime);
    letter-spacing: 1px;
    line-height: 1;
  }
  .contact .person {
    position: absolute;
    right: 38px;
    top: 150px;
    font-size: 21px;
    font-weight: 700;
    color: var(--white);
    text-transform: uppercase;
    letter-spacing: 0.5px;
  }
  .details {
    position: absolute;
    left: 28px;
    top: 152px;
    list-style: none;
    color: var(--white);
    font-size: 13px;
    font-weight: 400;
    line-height: 1.3;
  }
  .details li {
    display: flex;
    align-items: center;
    gap: 8px;
    margin-bottom: 9px;
  }
  .details li.gap-top { margin-top: 10px; }
  .icon {
    flex: none;
    width: 17px;
    height: 17px;
    border-radius: 50%;
    background: var(--white);
    display: flex;
    align-items: center;
    justify-content: center;
  }
  .icon svg { width: 11px; height: 11px; }

  /* role side */
  .roles .brand {
    position: absolute;
    left: 86px;
    top: 30px;
    font-size: 72px;
    font-weight: 300;
    color: var(--white);
    line-height: 1;
    letter-spacing: 1px;
  }
  .roles .web {
    position: absolute;
    left: 90px;
    top: 112px;
    font-size: 15px;
    font-weight: 300;
    color: var(--white);
    letter-spacing: 5px;
  }
  .role {
    position: absolute;
    width: 100px;
    height: 100px;
    border-radius: 50%;
    border: 3px solid var(--white);
    box-shadow: 0 0 0 1px rgba(0,0,0,0.06);
    display: flex;
    align-items: center;
    justify-content: center;
    text-align: center;
    color: var(--white);
    font-size: 11px;
    font-weight: 400;
    text-transform: uppercase;
    line-height: 1.2;
  }
  .role.team { left: 96px; top: 192px; background: var(--blue); }
  .role.manager { left: 238px; top: 166px; background: var(--orange); }
  .role.management { left: 378px; top: 140px; background: var(--lime-soft); }
</style>
</head>
<body>
<main class="sheet">

  <section class="card contact" aria-label="Card front with contact details">
    <svg class="card-shape" viewBox="0 0 540 309" aria-hidden="true">
      <path d="M0 140 H378 L394 116 V104 H540 V309 H0 Z" fill="var(--lime)"/>
    </svg>
    <div class="brand">Veltora</div>
    <div class="person">Marten Kuyvelsma</div>
    <ul class="details">
      <li>
        <span class="icon"><svg viewBox="0 0 12 12"><rect x="3.5" y="1" width="5" height="10" rx="1" fill="var(--lime)"/></svg></span>
        +31 (0) 6 927 15 062
      </li>
      <li>
        <span class="icon"><svg viewBox="0 0 12 12"><rect x="1" y="3" width="10" height="6.5" fill="var(--lime)"/><path d="M1 3 L6 7 L11 3" stroke="var(--white)" stroke-width="1" fill="none"/></svg></span>
        marten@veltora-demo.com
      </li>
      <li>
        <span class="icon"><svg viewBox="0 0 12 12"><path d="M6 11 C3 7 2.5 5.8 2.5 4.5 A3.5 3.5 0 0 1 9.5 4.5 C9.5 5.8 9 7 6 11 Z" fill="var(--lime)"/><circle cx="6" cy="4.5" r="1.3" fill="var(--white)"/></svg></span>
        <span>Oostelingpad 84c<br>2184 KT Duinwijk</span>
      </li>
      <li class="gap-top">
        <span class="icon"><svg viewBox="0 0 12 12"><path d="M3 1.5 L5 4 L4 5.2 C4.8 6.8 5.6 7.6 7 8.2 L8.2 7 L10.5 9 L9.2 10.5 C5.5 10 2 6.5 1.5 2.8 Z" fill="var(--lime)"/></svg></span>
        +31 (0)255 47 09 36
      </li>
    </ul>
  </section>

  <section class="card roles" aria-label="Card back with roles">
    <svg class="card-shape" viewBox="0 0 540 309" aria-hidden="true">
      <path d="M0 0 H540 V140 H262 L246 162 L230 140 H0 Z" fill="var(--lime)"/>
    </svg>
    <div class="brand">Veltora</div>
    <div class="web">www.veltora-demo.com</div>
    <div class="role team">Team<br>Member</div>
    <div class="role manager">Project<br>Manager</div>
    <div class="role management">Management</div>
  </section>

</main>
</body>
</html>
```